Disease outbreak warning

I need a flyer that explains to hunters how to act as frontline responders to potential disease outbreaks in wildlife populations. In this case the disease is African Swine Fever. We need an at a glance style with plenty of colour and that’s very easy to read.

I HAVE ATTACHED SOME EXISTING FLYERS FROM OVERSEAS ETC THAT CONTAIN SOME OF THE RELEVANT INFO. THEY ARE TO BE USED AS A GUIDE ONLY.
Updates

Need to see some more options. We have some that can be developed successfully but we’d like to see some more options that will suit a national campaign.

Target Market(s)

Australian hunters encountering wild pigs. Typical age is from 18 to 32 but can be older. Male or female.

Colors

Designer to choose colors to be used in the design.

Requirements
Must have
• The KVRTE logo (supplied). It should be relatively small at the bottom of the page. Plus we need room for two or three other logos that can be overprinted on the project if required.
• Must have information for hunters as the main focus.
Nice to have
• A double sided flyer.
Should not have
• US spelling.

```html
<!DOCTYPE html>
<html lang="en-AU">
<head>
<meta charset="utf-8">
<title>African Swine Fever – Hunter Trifold, Side 1</title>
<link href="https://fonts.googleapis.com/css2?family=Bebas+Neue&family=Oswald:wght@400;500;600&display=swap" rel="stylesheet">
<style>
  :root {
    --red: #d8232a;
    --red-deep: #a3161b;
    --ink: #1c1c1c;
    --charcoal: #2e2e2e;
    --paper: #f4f4f2;
    --white: #ffffff;
    --stage: #e6e6e6;
  }
  * { box-sizing: border-box; margin: 0; padding: 0; }
  html, body { width: 1200px; height: 800px; overflow: hidden; background: var(--stage); }
  .sheet {
    position: absolute; left: 30px; top: 20px;
    width: 1140px; height: 760px;
    display: flex; background: var(--paper);
  }
  .panel { position: relative; width: 380px; height: 760px; overflow: hidden; }

  /* Panel 1 – precautions */
  .precautions { background: var(--paper); padding: 34px 30px 0 30px; }
  .headline { font-family: "Bebas Neue", sans-serif; line-height: .9; }
  .precautions .kicker { font-size: 46px; color: var(--ink); }
  .precautions .title { font-size: 70px; color: var(--red); }
  .steps { list-style: none; margin-top: 26px; }
  .step { display: flex; align-items: center; gap: 18px; height: 84px; }
  .step-icon { flex: 0 0 64px; width: 64px; height: 64px; background: var(--red); display: flex; align-items: center; justify-content: center; }
  .step-text { font-family: "Oswald", sans-serif; font-weight: 500; font-size: 15px; line-height: 1.25; text-transform: uppercase; color: var(--ink); }

  /* Panel 2 – about the disease */
  .about { background: var(--paper); }
  .about-intro { padding: 40px 30px 0 30px; font-family: "Oswald", sans-serif; font-weight: 600; font-size: 18px; line-height: 1.3; text-transform: uppercase; color: var(--ink); }
  .about-intro .alert { color: var(--red); }
  .pig-mark { display: block; width: 96px; height: 54px; margin: 18px auto 0; background: var(--red); border-radius: 27px; }
  .responder { position: absolute; left: 0; top: 420px; width: 380px; height: 340px; background: linear-gradient(160deg, #4a4a4a 0%, var(--charcoal) 55%, #222 100%); }
  .responder-copy { padding: 26px 30px 0; font-family: "Oswald", sans-serif; font-weight: 500; font-size: 17px; line-height: 1.35; text-transform: uppercase; color: var(--white); }
  .cta-band { position: absolute; left: 0; top: 150px; width: 380px; height: 130px; background: var(--red); padding: 14px 26px 0; }
  .cta-band .small { font-size: 38px; color: var(--ink); }
  .cta-band .big { font-size: 86px; color: var(--white); }

  /* Panel 3 – cover */
  .cover { background: var(--paper); }
  .cover-photo { position: absolute; left: 0; top: 0; width: 380px; height: 380px; background: linear-gradient(180deg, #7a9bb0 0%, #5c6e47 35%, #2f2a26 75%, #3b3330 100%); }
  .cover-photo-edge { position: absolute; right: 0; top: 0; width: 70px; height: 380px; background: linear-gradient(180deg, var(--red-deep), #5e0e10); }
  .brand { position: absolute; left: 26px; top: 26px; display: flex; align-items: center; gap: 10px; }
  .brand-dot { width: 34px; height: 34px; border-radius: 50%; background: var(--white); }
  .brand-name { font-family: "Bebas Neue", sans-serif; font-size: 34px; color: var(--white); }
  .cover-rule { position: absolute; left: 0; top: 380px; width: 380px; height: 10px; background: var(--red); }
  .cover-copy { position: absolute; left: 0; top: 400px; width: 380px; text-align: center; }
  .cover-copy .l1 { font-size: 44px; color: var(--ink); }
  .cover-copy .l2 { font-size: 46px; color: var(--red); }
  .cover-copy .l3 { font-size: 78px; color: var(--red); margin-top: 6px; }
  .cover-copy .l4 { font-size: 50px; color: var(--ink); }
  .cover-copy .l5 { font-size: 33px; color: var(--ink); }
  .cover-copy .l6 { font-size: 56px; color: var(--red); }
  .cover-base { position: absolute; left: 30px; top: 706px; width: 320px; height: 5px; background: var(--ink); }
  .web { position: absolute; left: 0; top: 718px; width: 380px; text-align: center; font-family: "Oswald", sans-serif; font-weight: 500; font-size: 18px; letter-spacing: 5px; color: var(--ink); }
  .web span { color: var(--red); }
</style>
</head>
<body>
<main class="sheet">

  <section class="panel precautions">
    <h2 class="headline"><span class="kicker">Respect general</span><br><span class="title">Precautions</span></h2>
    <ul class="steps">
      <li class="step">
        <span class="step-icon"><svg width="40" height="40" viewBox="0 0 40 40"><path d="M20 4 C28 16 32 22 32 27 A12 12 0 0 1 8 27 C8 22 12 16 20 4Z" fill="#fff"/></svg></span>
        <p class="step-text">Clean and disinfect your equipment on site</p>
      </li>
      <li class="step">
        <span class="step-icon"><svg width="40" height="40" viewBox="0 0 40 40"><path d="M6 21 L16 31 L34 9" stroke="#fff" stroke-width="6" fill="none" stroke-linecap="round" stroke-linejoin="round"/></svg></span>
        <p class="step-text">Clean and disinfect your hunting trophies before leaving the area</p>
      </li>
      <li class="step">
        <span class="step-icon"><svg width="40" height="40" viewBox="0 0 40 40"><rect x="5" y="5" width="30" height="30" fill="none" stroke="#fff" stroke-width="4"/><path d="M10 10 L30 30 M30 10 L10 30" stroke="#fff" stroke-width="4"/></svg></span>
        <p class="step-text">Do not visit farms unless it necessary</p>
      </li>
      <li class="step">
        <span class="step-icon"><svg width="40" height="40" viewBox="0 0 40 40"><path d="M20 37 C10 24 8 19 8 15 A12 12 0 0 1 32 15 C32 19 30 24 20 37Z" fill="#fff"/><circle cx="20" cy="15" r="5" fill="#d8232a"/></svg></span>
        <p class="step-text">Eviscerate shot wild boar in the designated dressing area of the hunting ground</p>
      </li>
      <li class="step">
        <span class="step-icon"><svg width="40" height="40" viewBox="0 0 40 40"><rect x="6" y="22" width="28" height="10" rx="2" fill="#fff"/><path d="M12 18 L28 18" stroke="#fff" stroke-width="3"/><path d="M14 6 L26 16 M26 6 L14 16" stroke="#fff" stroke-width="3"/></svg></span>
        <p class="step-text">Do not leave food for wild boar</p>
      </li>
      <li class="step">
        <span class="step-icon"><svg width="44" height="44" viewBox="0 0 44 44"><path d="M10 22 A12 12 0 0 1 30 12" stroke="#fff" stroke-width="5" fill="none"/><path d="M27 5 L34 13 L24 16Z" fill="#fff"/><path d="M34 22 A12 12 0 0 1 14 32" stroke="#fff" stroke-width="5" fill="none"/><path d="M17 39 L10 31 L20 28Z" fill="#fff"/></svg></span>
        <p class="step-text">Do not share home-made products from your hunt or feed them to animals</p>
      </li>
    </ul>
  </section>

  <section class="panel about">
    <p class="about-intro">
      African swine fever (ASF) is a highly contagious disease of domestic and wild pigs, it is not a danger to human health but is devastating for farming economy.
      <span class="alert">There is no vaccine against it. Lorem and type setting industry. Lorem Ipsum has been the industry's industry.</span>
    </p>
    <span class="pig-mark" role="img" aria-label="Red pig silhouette"></span>
    <div class="responder" role="img" aria-label="Dark toned photograph of a pig behind the text">
      <p class="responder-copy">As humans, you have both the opportunity to detect cases early and the responsiblity to act appropriately.</p>
      <div class="cta-band">
        <h2 class="headline"><span class="small">Don't spread the</span><br><span class="big">Disease</span></h2>
      </div>
    </div>
  </section>

  <section class="panel cover">
    <div class="cover-photo" role="img" aria-label="Photograph of a wild boar lying on a log in open bushland"></div>
    <div class="cover-photo-edge"></div>
    <div class="brand"><span class="brand-dot"></span><span class="brand-name">KVRTE</span></div>
    <div class="cover-rule"></div>
    <h1 class="cover-copy headline">
      <span class="l1">African swine fever</span><br>
      <span class="l2">Kills pigs</span><br>
      <span class="l3">Hunters</span><br>
      <span class="l4">Don't be the</span><br>
      <span class="l5">Carrier of a deadly</span><br>
      <span class="l6">Pig disease</span>
    </h1>
    <div class="cover-base"></div>
    <p class="web">WWW.<span>KVRTE.ORG</span>.AU</p>
  </section>

</main>
</body>
</html>
```